Wholesale Fashion Agent

Industry/Entity Type

Fashion

Contact Information for Business Card

I have attached the previous logo, we are wanting to re-vamp with black and white only. Sharp and more modern.

Marisa Tolkett Agencies back of card
address (to be advised, as we are moving)

MT Agencies front of card, with Fashion Agent on the front

```html
<!DOCTYPE html>
<html lang="en">
<head>
<meta charset="utf-8">
<title>MT Agencies – Business Cards</title>
<link rel="stylesheet" href="https://fonts.googleapis.com/css2?family=Cormorant+Garamond:wght@500&family=Source+Sans+3:wght@400;600&display=swap">
<style>
  :root {
    --backdrop: #e4e2df;
    --card: #141414;
    --card-edge: #1c1c1c;
    --ink: #f4f4f4;
    --ink-soft: #cfcfcf;
    --silver: #b9b9b9;
    --rule: #5a5a5a;
  }
  * { margin: 0; padding: 0; box-sizing: border-box; }
  html, body {
    width: 1200px; height: 844px; overflow: hidden;
    background: var(--backdrop);
  }
  .canvas {
    position: relative; width: 1200px; height: 844px;
  }
  .card {
    position: absolute; top: 267px;
    width: 540px; height: 309px;
    background: linear-gradient(135deg, var(--card-edge), var(--card));
    box-shadow: 0 6px 18px rgba(0,0,0,0.25);
    color: var(--ink);
    font-family: "Source Sans 3", sans-serif;
  }
  .card--front { left: 40px; }
  .card--back { left: 620px; }

  /* brand block */
  .brand { position: absolute; display: flex; align-items: center; gap: 16px; }
  .brand__square { background: var(--ink); flex: none; }
  .brand__text { display: flex; flex-direction: column; }
  .brand__name {
    font-family: "Cormorant Garamond", serif; font-weight: 500;
    letter-spacing: 1px; line-height: 1; white-space: nowrap;
  }
  .brand__rule { height: 1px; background: var(--rule); margin: 6px 0 5px; }
  .brand__tagline {
    font-family: "Source Sans 3", sans-serif;
    letter-spacing: 1.5px; text-transform: uppercase; text-align: center;
  }

  .card--front .brand { left: 40px; top: 52px; }
  .card--front .brand__square { width: 72px; height: 72px; }
  .card--front .brand__name { font-size: 31px; color: var(--ink); }
  .card--front .brand__tagline { font-size: 9px; color: var(--ink-soft); }

  .card--back .brand { left: 50%; top: 50%; transform: translate(-50%, -50%); }
  .card--back .brand__square { width: 56px; height: 56px; background: var(--silver); }
  .card--back .brand__name { font-size: 30px; color: var(--silver); }
  .card--back .brand__tagline { font-size: 9px; color: #8c8c8c; }

  /* person */
  .person {
    position: absolute; left: 30px; top: 160px; width: 200px;
    text-align: right;
  }
  .person__name { font-size: 21px; font-weight: 600; line-height: 1.1; }
  .person__title { font-size: 14px; color: var(--ink-soft); margin-bottom: 10px; }
  .person__address { font-size: 15px; line-height: 1.15; }

  .divider {
    position: absolute; left: 248px; top: 160px;
    width: 1px; height: 112px; background: var(--rule);
  }

  /* contacts */
  .contacts {
    position: absolute; left: 266px; top: 160px;
    list-style: none; font-size: 14.5px; line-height: 24px;
  }
  .contacts li { display: flex; align-items: center; gap: 9px; }
  .contacts svg { width: 11px; height: 11px; fill: var(--ink); flex: none; }
</style>
</head>
<body>
<main class="canvas">

  <section class="card card--front" aria-label="Business card front">
    <div class="brand">
      <span class="brand__square"></span>
      <div class="brand__text">
        <span class="brand__name">MT AGENCIES</span>
        <span class="brand__rule"></span>
        <span class="brand__tagline">Fashion Agent</span>
      </div>
    </div>

    <div class="person">
      <p class="person__name">Daniel Harper</p>
      <p class="person__title">Managing Director</p>
      <p class="person__address">18 Harbour Lane<br>Northvale, 40210</p>
    </div>

    <span class="divider"></span>

    <ul class="contacts">
      <li>
        <svg viewBox="0 0 12 12" aria-hidden="true"><path d="M1 3.5C1 2 2.5 1 6 1s5 1 5 2.5V5H8.5V4h-5v1H1z M2.5 6h7l1 5h-9z"/></svg>
        (044)-555-0190
      </li>
      <li>
        <svg viewBox="0 0 12 12" aria-hidden="true"><path d="M3 0h6v12H3z M4 1.5v7.5h4V1.5z" fill-rule="evenodd"/></svg>
        123-555-0147
      </li>
      <li>
        <svg viewBox="0 0 12 12" aria-hidden="true"><path d="M0 2h12v8H0z M1 3l5 4 5-4" /></svg>
        info@mtagencies.example
      </li>
      <li>
        <svg viewBox="0 0 12 12" aria-hidden="true"><path d="M6 0a6 6 0 1 0 0 12A6 6 0 0 0 6 0z M6 1.3a4.7 4.7 0 1 1 0 9.4 4.7 4.7 0 0 1 0-9.4z" fill-rule="evenodd"/></svg>
        www.mtagencies.example
      </li>
    </ul>
  </section>

  <section class="card card--back" aria-label="Business card back">
    <div class="brand">
      <span class="brand__square"></span>
      <div class="brand__text">
        <span class="brand__name">MT AGENCIES</span>
        <span class="brand__rule"></span>
        <span class="brand__tagline">Fashion Agent</span>
      </div>
    </div>
  </section>

</main>
</body>
</html>
```